Website for my law practice

I am a solo practitioner, who specializes in family law and estate planning in Massachusetts. I need to re-do my website, as it is outdated. I like the idea of a nontraditional law firm website. My website address is: rosalindhartwelllaw.com. I would like to retain my logo in the green color, as part of the new website. I have uploaded my logo below.
Updates

My hourly rate has changed from what is listed on my current website. My new hourly rate is $385.00. Please use this hourly rate when creating the website.

Good morning,

I have reviewed the designs submitted so far. I am happy that the "rh" logo in the green color is part of each of the designs submitted. I am also happy that the standard items seen in law firm websites, such as the scales of justice, etc. were not incorporated. Although the green logo is great, I do not think rest of the website has to have the same green color throughout. Additionally, I was hoping for something more creative, to make the website standout and not the stock web designs you see everyday. Please incorporate more unique images if you can. For example of what I mean, please look at this website: https://www.lorettafinchlaw.com

Coding

```html
<!DOCTYPE html>
<html lang="en">
<head>
<meta charset="utf-8">
<title>Rosalind Hartwell, Attorney at Law</title>
<link href="https://fonts.googleapis.com/css2?family=Poppins:wght@300;400;500;600;700&display=swap" rel="stylesheet">
<style>
:root{
  --green:#1f8a22;
  --green-dark:#17701a;
  --ink:#1d1d1d;
  --text:#555;
  --hero:#1c1c1c;
  --white:#fff;
  --line:#d9d9d9;
}
*{box-sizing:border-box;margin:0;padding:0}
html,body{width:1200px;height:4916px;overflow:hidden}
body{position:relative;font-family:"Poppins",sans-serif;color:var(--text);background:var(--white);font-size:14px;line-height:1.7}
.abs{position:absolute}
.photo{position:absolute}
a{color:inherit;text-decoration:none}

.btn{display:inline-flex;align-items:center;gap:8px;background:var(--green);color:var(--white);border-radius:24px;font-size:13px;font-weight:500;padding:10px 22px;letter-spacing:.5px}
.btn svg{width:12px;height:12px}

/* nav */
.nav{left:0;top:0;width:1200px;height:144px;background:var(--white)}
.brand{left:60px;top:50px;display:flex;align-items:center;gap:12px}
.brand-mark{width:40px;height:40px;border-radius:50%;background:var(--green)}
.brand-name{color:var(--green);font-weight:600;font-size:14px;line-height:1.25}
.menu{left:378px;top:68px;display:flex;gap:38px;font-size:13px;color:var(--ink);font-weight:500}
.menu .active{color:var(--green);border-bottom:2px solid var(--green);padding-bottom:2px}
.call{left:915px;top:20px;display:flex;align-items:center;gap:8px;color:var(--green);font-weight:600;font-size:15px}
.call span.ic{width:28px;height:28px;border:1px solid var(--green);border-radius:50%;display:flex;align-items:center;justify-content:center}
.nav-contact{left:1020px;top:64px;padding:6px 18px;font-size:12px}

/* hero */
.hero{left:0;top:144px;width:1200px;height:744px;background:var(--hero)}
.hero-intro{left:70px;top:150px;width:640px;color:var(--green);font-size:26px;font-weight:500;line-height:1.4}
.hero-title{left:70px;top:265px;color:var(--white);font-size:56px;font-weight:600;line-height:1.2;letter-spacing:1px}
.hero-btn{left:70px;top:460px}
.hero-photo{left:712px;top:16px;width:432px;height:728px;background:linear-gradient(160deg,#c9d7e2,#9eb0bf 45%,#6f5a4a)}
.dots{fill:#444}

/* about */
.about-ring{left:66px;top:975px;width:445px;height:445px;border-radius:50%;border:3px solid var(--green)}
.about-photo{left:108px;top:1017px;width:361px;height:361px;border-radius:50%;background:radial-gradient(circle at 50% 40%,#d0d0d0,#8a8a8a 60%,#5a5a5a)}
.about-dot{left:98px;top:1336px;width:24px;height:24px;border-radius:50%;background:var(--green)}
.section-title{color:var(--ink);font-weight:400;font-size:44px;letter-spacing:1px;line-height:1.1}
.section-sub{color:var(--green);font-weight:600;font-size:15px}
.about-head{left:565px;top:1000px}
.about-text{left:565px;top:1128px;width:540px;font-size:12.5px;line-height:1.75}
.about-btn{left:565px;top:1340px}
.badge{left:780px;top:1300px;width:140px;height:100px;border-radius:50%;background:#d9c070}

/* consultation */
.consult{left:64px;top:1532px;width:1072px;height:316px;background:var(--green);border-radius:28px}
.consult h2{position:absolute;left:0;top:36px;width:100%;text-align:center;color:var(--white);font-weight:400;font-size:34px;letter-spacing:1px}
.consult-card{position:absolute;left:30px;top:104px;width:1012px;height:186px;border:2px solid var(--white);border-radius:22px;text-align:center;color:var(--white);padding:26px 60px;font-size:13px}
.consult-card .btn{background:transparent;border:1.5px solid var(--white);margin-top:18px}

/* family */
.family-head{left:70px;top:2020px}
.family-text{left:70px;top:2140px;width:600px;font-size:12.5px}
.family-btn{left:70px;top:2310px}
.family-photo{left:780px;top:1960px;width:332px;height:312px;background:linear-gradient(135deg,#5a4a8a,#3e3070 50%,#d8d8e0)}
.family-box{left:680px;top:2272px;width:210px;height:328px;background:var(--green);padding:30px 18px;color:var(--white);font-size:13px}
.service-item{display:flex;align-items:center;gap:12px;margin-bottom:34px;line-height:1.3}
.service-ic{flex:none;width:36px;height:36px;border-radius:50%;background:var(--white);display:flex;align-items:center;justify-content:center}

/* estate */
.estate-photo{left:68px;top:2600px;width:324px;height:308px;background:linear-gradient(150deg,#b8b0a2,#6b6f80 55%,#3d4a66)}
.estate-box{left:132px;top:2852px;width:300px;height:528px;background:var(--green);color:var(--white);font-size:12.5px;padding:30px 24px}
.estate-box li{list-style:none;display:flex;gap:10px;align-items:flex-start;margin-bottom:20px;line-height:1.3}
.estate-box li::before{content:"";flex:none;width:8px;height:8px;border-radius:2px;background:var(--white);margin-top:5px}
.estate-head{left:552px;top:2725px}
.estate-text{left:552px;top:2815px;width:580px;font-size:12.5px}
.estate-text p{margin-bottom:14px}
.estate-btn{left:552px;top:3020px}

/* faq */
.faq-head{left:70px;top:3540px}
.faq-list{left:70px;top:3640px;width:660px;font-size:13px}
.faq-q{display:flex;gap:10px;color:var(--ink);font-weight:600;padding:12px 0;border-bottom:1px solid var(--line)}
.faq-q svg{flex:none;margin-top:5px}
.faq-q.open{color:var(--green);border:none}
.faq-a{font-size:12px;padding:0 0 12px 22px;border-bottom:1px solid var(--line)}
.faq-photo{left:780px;top:3520px;width:364px;height:448px;border-radius:10px;background:linear-gradient(135deg,#e9e4dc,#c7b9a8 55%,#8a7260)}

/* contact */
.green-band{left:0;top:4520px;width:1200px;height:396px;background:var(--green)}
.contact-photo{left:68px;top:4152px;width:468px;height:468px;background:linear-gradient(180deg,#c6d6e6,#b9a690 55%,#6f5d4b)}
.contact-card{left:540px;top:4152px;width:592px;height:488px;background:var(--white);box-shadow:0 6px 24px rgba(0,0,0,.12);padding:50px 55px}
.contact-card h2{color:var(--ink);font-weight:400;font-size:40px;letter-spacing:1px;margin-bottom:26px}
.field{border:1px solid var(--line);height:40px;font-size:12px;color:#999;padding:10px 12px;margin-bottom:14px}
.row{display:flex;gap:12px}.row .field{flex:1}
.field.msg{height:100px}

/* footer */
.foot-col{color:var(--white);font-size:12.5px}
.foot-col h4{font-size:14px;font-weight:600;margin-bottom:10px}
.foot-col li{list-style:none;display:flex;gap:8px;align-items:center;margin-bottom:2px}
.foot-col li::before{content:"";width:6px;height:6px;border-radius:50%;background:var(--white)}
.foot-links{left:230px;top:4680px}
.foot-brand{left:500px;top:4660px;width:200px;text-align:center;color:var(--white);font-weight:600;font-size:16px;line-height:1.3}
.foot-brand .brand-mark{margin:0 auto 14px;width:56px;height:56px;background:var(--white)}
.foot-contact{left:835px;top:4680px}
.foot-contact .c{display:flex;gap:10px;margin-bottom:8px;line-height:1.35}
.foot-contact .ci{flex:none;width:22px;height:22px;border-radius:50%;border:1px solid var(--white)}
.copyright{left:0;top:4874px;width:1200px;text-align:center;color:var(--white);font-size:12px;border-top:1px solid rgba(255,255,255,.35);padding-top:10px}
</style>
</head>
<body>

<header class="abs nav">
  <div class="abs brand"><span class="brand-mark"></span><span class="brand-name">Rosalind Hartwell<br>Attorney at Law</span></div>
  <nav class="abs menu">
    <a class="active">HOME</a><a>FAMILY LAW</a><a>ESTATE PLANNING</a><a>ABOUT</a><a>LOCATION</a><a>FAQ</a>
  </nav>
  <div class="abs call"><span class="ic"><svg width="13" height="13" viewBox="0 0 24 24"><path fill="#1f8a22" d="M6.6 10.8a15 15 0 0 0 6.6 6.6l2.2-2.2a1 1 0 0 1 1-.25 11.4 11.4 0 0 0 3.6.57 1 1 0 0 1 1 1V20a1 1 0 0 1-1 1A17 17 0 0 1 3 4a1 1 0 0 1 1-1h3.5a1 1 0 0 1 1 1c0 1.25.2 2.45.57 3.57a1 1 0 0 1-.25 1z"/></svg></span>CALL US : (555) 014-2290</div>
  <a class="abs btn nav-contact">CONTACT</a>
</header>

<section class="abs hero">
  <svg class="abs" style="left:1050px;top:20px" width="120" height="60"><g class="dots"><circle cx="5" cy="5" r="2"/><circle cx="20" cy="5" r="2"/><circle cx="35" cy="5" r="2"/><circle cx="50" cy="5" r="2"/><circle cx="5" cy="20" r="2"/><circle cx="20" cy="20" r="2"/><circle cx="35" cy="20" r="2"/><circle cx="50" cy="20" r="2"/></g></svg>
  <p class="abs hero-intro">Rosalind Hartwell is a Solo Practitioner focusing her practice on matters pertaining to</p>
  <h1 class="abs hero-title">FAMILY LAW AND<br>ESTATE PLANNING.</h1>
  <a class="abs btn hero-btn">CONTACT US <svg viewBox="0 0 12 12"><path d="M2 10L10 2M4 2h6v6" stroke="#fff" stroke-width="1.6" fill="none"/></svg></a>
  <div class="photo hero-photo" role="img" aria-label="Portrait of the attorney smiling outdoors by the water"></div>
</section>

<div class="abs about-ring"></div>
<div class="photo about-photo" role="img" aria-label="Black and white portrait of the attorney"></div>
<div class="abs about-dot"></div>
<div class="abs about-head"><h2 class="section-title">ABOUT ME</h2><p class="section-sub">Who Am I</p></div>
<p class="abs about-text">Rosalind is a graduate of Harborview University in Boston, Massachusetts. She received her Bachelor of Science degree in Criminal Justice and a minor in Political Science in 1993. While attending Harborview, Rosalind was a Harborview Merit Scholar, graduating from the University Magna Cum Laude. Rosalind obtained her Juris Doctor from Bayline School of Law in Boston, Massachusetts in 1996. During her law school career, she interned at the Office of Coastal Resources in Boston, Massachusetts.</p>
<a class="abs btn about-btn">KNOW MORE <svg viewBox="0 0 12 12"><path d="M2 10L10 2M4 2h6v6" stroke="#fff" stroke-width="1.6" fill="none"/></svg></a>
<div class="abs badge" role="img" aria-label="Recognition badge"></div>

<section class="abs consult">
  <h2>FREE 30-MINUTE CONSULTATION</h2>
  <div class="consult-card">
    <p>I respect the fact that your time is valuable. Therefore, I provide a free 30-minute consultation to potential clients. The consultation is a great way to learn more about what options there are for your issue, as well as for both you and I to see if we are a good fit.</p>
    <a class="btn">CONTACT ME <svg viewBox="0 0 12 12"><path d="M2 10L10 2M4 2h6v6" stroke="#fff" stroke-width="1.6" fill="none"/></svg></a>
  </div>
</section>

<div class="abs family-head"><h2 class="section-title">FAMILY LAW</h2><p class="section-sub">Why Hiring an Attorney is the Right Choice</p></div>
<p class="abs family-text">Going through a divorce is difficult. Especially in cases where there are minor children or complicated financial holdings, questions will arise that you may not be prepared to answer without the assistance of a knowledgeable and reputable advocate. Some of the questions that may arise are: will one party remain in the family home or will it be sold? Who will be the primary caretaker of the children? How will custody decisions be affected if one party moves to a different town or state?</p>
<a class="abs btn family-btn">KNOW MORE <svg viewBox="0 0 12 12"><path d="M2 10L10 2M4 2h6v6" stroke="#fff" stroke-width="1.6" fill="none"/></svg></a>
<div class="photo family-photo" role="img" aria-label="Family law reference books stacked on a desk"></div>
<div class="abs family-box">
  <div class="service-item"><span class="service-ic"><svg width="16" height="16" viewBox="0 0 16 16"><rect x="3" y="1" width="10" height="14" rx="1" fill="none" stroke="#1f8a22" stroke-width="1.5"/><path d="M5 5h6M5 8h6M5 11h4" stroke="#1f8a22" stroke-width="1.3"/></svg></span>Pre and Post Nuptial Agreements</div>
  <div class="service-item"><span class="service-ic"><svg width="16" height="16" viewBox="0 0 16 16"><rect x="3" y="1" width="10" height="14" rx="1" fill="none" stroke="#1f8a22" stroke-width="1.5"/><path d="M5 5h6M5 8h6M5 11h4" stroke="#1f8a22" stroke-width="1.3"/></svg></span>Divorce</div>
  <div class="service-item"><span class="service-ic"><svg width="16" height="16" viewBox="0 0 16 16"><rect x="3" y="1" width="10" height="14" rx="1" fill="none" stroke="#1f8a22" stroke-width="1.5"/><path d="M5 5h6M5 8h6M5 11h4" stroke="#1f8a22" stroke-width="1.3"/></svg></span>Post-Divorce</div>
</div>

<div class="photo estate-photo" role="img" aria-label="Book on drafting wills and trusts"></div>
<ul class="abs estate-box">
  <li>Will</li>
  <li>Durable Power of Attorney with Nomination of Guardian</li>
  <li>Health Care Proxy</li>
  <li>Memorandum of Remains</li>
  <li>Revocable Living Trust</li>
  <li>Irrevocable Living Trust</li>
  <li>Trustee's Certificate</li>
  <li>Quitclaim Deed</li>
  <li>Trust Amendments</li>
</ul>
<div class="abs estate-head"><h2 class="section-title">ESTATE PLANNING</h2></div>
<div class="abs estate-text">
  <p>Whether you are creating an estate plan for the first time or updating your existing plan, I strive to make the estate planning process easy to understand, comfortable and comprehensive.</p>
  <p>Throughout the process of drafting an estate plan, additional professionals such as a financial planner, CPA and life insurance agent may become necessary resources in the handling of your assets.</p>
</div>
<a class="abs btn estate-btn">KNOW MORE <svg viewBox="0 0 12 12"><path d="M2 10L10 2M4 2h6v6" stroke="#fff" stroke-width="1.6" fill="none"/></svg></a>

<div class="abs faq-head"><h2 class="section-title">FAQ</h2></div>
<div class="abs faq-list">
  <div class="faq-q open"><svg width="10" height="10" viewBox="0 0 10 10"><path d="M1 3l4 4 4-4" stroke="#1f8a22" stroke-width="1.6" fill="none"/></svg>What will a divorce cost me?</div>
  <p class="faq-a">I currently bill my family law clients at <span style="color:var(--green)">$385.00 per hour</span>. Although I will make every effort to keep costs reasonable for you and work within the agreed upon retainer, I cannot give you a fixed price for a divorce (or any other family law matter). The reason is because I cannot predict what the opposition will file during the litigation process, or what pleadings I may need to file on your behalf in order to achieve your goals in this matter.</p>
  <div class="faq-q"><svg width="10" height="10" viewBox="0 0 10 10"><path d="M3 1l4 4-4 4" stroke="#1d1d1d" stroke-width="1.6" fill="none"/></svg>How long will it take for me to get divorced?</div>
  <div class="faq-q"><svg width="10" height="10" viewBox="0 0 10 10"><path d="M3 1l4 4-4 4" stroke="#1d1d1d" stroke-width="1.6" fill="none"/></svg>What kinds of information should I bring with me for my free 30-minute consultation?</div>
</div>
<div class="photo faq-photo" role="img" aria-label="Attorney meeting with a couple in an office"></div>

<div class="abs green-band"></div>
<div class="photo contact-photo" role="img" aria-label="Street view of the office building"></div>
<form class="abs contact-card">
  <h2>CONTACT</h2>
  <div class="row"><div class="field">Your Name</div><div class="field">Phone Number</div></div>
  <div class="field">Email Address</div>
  <div class="field msg">Message</div>
  <span class="btn" style="padding:7px 20px;font-size:12px">SUBMIT <svg viewBox="0 0 12 12"><path d="M2 10L10 2M4 2h6v6" stroke="#fff" stroke-width="1.6" fill="none"/></svg></span>
</form>

<div class="abs foot-col foot-links">
  <h4>QUICK LINKS</h4>
  <ul><li>About</li><li>Family Law</li><li>Estate Planning</li><li>Location</li><li>Contact</li></ul>
</div>
<div class="abs foot-brand"><div class="brand-mark"></div>Rosalind Hartwell<br>Attorney at Law</div>
<div class="abs foot-col foot-contact">
  <h4>CONTACT US</h4>
  <div class="c"><span class="ci"></span><span>Call Us : (555) 014-2290<br>Fax Us : (555) 014-2291</span></div>
  <div class="c"><span class="ci"></span><span>Email Us :<br>rosalind@rosalindhartwelllaw.com</span></div>
  <div class="c"><span class="ci"></span><span>42 Linden Street<br>Maple Falls, MA 01900</span></div>
</div>
<p class="abs copyright">Copyright © 2020 All Rights Reserved by Rosalind Hartwell</p>

</body>
</html>
```